job vacancy cover page

I need to design a one pager for a job I'd like to apply for. The one I have done looks shit and amateur!! Wanting it to look amazing and professional (Not too professional though as they are pretty young and fun).

```html
<!DOCTYPE html>
<html lang="en">
<head>
<meta charset="utf-8">
<title>Lantern Row – Why me?</title>
<link rel="stylesheet" href="https://fonts.googleapis.com/css2?family=Libre+Baskerville:wght@700&family=Nunito+Sans:wght@400;700&display=swap">
<style>
  :root {
    --ink: #1f1f1f;
    --header-bg: #252525;
    --sky: #dae6ee;
    --cream: #fdf3e9;
    --blush: #fde1ee;
    --brand-blue: #0a82bd;
    --tick-blue: #1e8fd0;
    --heart-top: #f34a9a;
    --heart-bottom: #cc1146;
    --footer-bg: #dcdee1;
    --divider-blue: #d4e3ee;
    --divider-pink: #f5dbe7;
    --serif: "Libre Baskerville", Georgia, serif;
    --sans: "Nunito Sans", Arial, sans-serif;
  }
  * { box-sizing: border-box; margin: 0; padding: 0; }
  html, body { width: 1200px; height: 1031px; overflow: hidden; background: #fff; }
  body { position: relative; font-family: var(--sans); color: var(--ink); }
  .abs { position: absolute; }
  ul { list-style: none; }

  .topbar { left: 0; top: 0; width: 1200px; height: 55px; background: var(--header-bg); color: #fff; font-family: var(--serif); }
  .brand { position: absolute; left: 30px; top: 13px; font-size: 22px; font-weight: 700; letter-spacing: -0.3px; }
  .page-title { position: absolute; left: 0; width: 1200px; top: 9px; text-align: center; font-size: 29px; font-weight: 700; }

  .panel { top: 55px; height: 451px; overflow: hidden; }
  .panel-hero { left: 0; width: 401px; background: var(--sky); }
  .panel-success { left: 402px; width: 400px; background: var(--cream); }
  .panel-passion { left: 803px; width: 397px; background: var(--blush); }

  .serif-heading { font-family: var(--serif); font-weight: 700; color: var(--ink); letter-spacing: -0.4px; }
  .rule { position: absolute; height: 1px; background: var(--ink); }
  .text-layer { z-index: 2; }
  .tick { display: block; width: 16px; height: 16px; }

  /* Superhero panel */
  .hero-title { left: 28px; top: 34px; font-size: 26px; line-height: 32px; }
  .hero-intro { left: 31px; top: 140px; font-size: 17px; line-height: 25.6px; }
  .hero-item { left: 29px; font-size: 17px; line-height: 22px; display: flex; align-items: center; gap: 13px; white-space: nowrap; }
  .hero-figure { left: 222px; top: 36px; width: 166px; height: 380px; border-radius: 80px 80px 30px 30px;
    background: linear-gradient(165deg, #2a8fd6 0%, #2a8fd6 60%, #e5222f 100%); opacity: .85; z-index: 1; }

  /* Success panel */
  .success-title { left: 40px; top: 62px; font-size: 26px; line-height: 32px; }
  .success-item { left: 45px; font-size: 13.6px; line-height: 19px; display: flex; gap: 7px; white-space: nowrap; }
  .success-item .tick { margin-top: 4px; }
  .trophy-figure { left: 252px; top: 34px; width: 132px; height: 384px; border-radius: 66px 66px 10px 10px;
    background: linear-gradient(180deg, #f3b46b 0%, #e8f2f8 35%, #3b2530 100%); opacity: .9; z-index: 1; }

  /* Passion panel */
  .passion-title { left: 0; width: 397px; top: 33px; text-align: center; font-size: 26px; line-height: 34px; }
  .heart { left: 0; top: 67px; }
  .passion-item { left: 0; width: 397px; text-align: center; color: #fff; font-size: 14px; line-height: 19px; }
  .passion-item .tick { margin: 0 auto 10px; }

  .divider { top: 506px; width: 1px; height: 452px; }
  .divider-a { left: 401px; background: var(--divider-blue); }
  .divider-b { left: 802px; background: var(--divider-pink); }

  .section-title { left: 0; width: 1216px; top: 547px; text-align: center; font-size: 24px; }

  /* Feature columns */
  .feature { top: 617px; width: 340px; }
  .feature-values { left: 61px; }
  .feature-offer { left: 459px; }
  .feature-projects { left: 865px; }
  .feature-icon { display: block; width: 84px; height: 84px; }
  .feature-heading { font-size: 17px; line-height: 24px; margin-top: 27px; }
  .feature-rule { width: 51px; height: 1px; background: var(--ink); margin-top: 9px; margin-bottom: 19px; }
  .feature-list li { height: 25.6px; display: flex; align-items: center; gap: 9px; font-size: 14px; white-space: nowrap; }
  .feature-list .tick { color: var(--tick-blue); }
  .project { font-size: 12.3px; line-height: 16px; margin-top: -2px; margin-bottom: 12px; }
  .project strong { display: block; font-size: 13.6px; line-height: 19px; }

  .footer { left: 0; top: 958px; width: 1200px; height: 73px; background: var(--footer-bg); }
  .copyright { position: absolute; left: 0; width: 1200px; top: 28px; text-align: center; font-size: 11px; color: #333; }
</style>
</head>
<body>
  <svg width="0" height="0" style="position:absolute">
    <defs>
      <symbol id="tick" viewBox="0 0 20 20">
        <path d="M17.5 8.5A7.8 7.8 0 1 1 13 2.8" fill="none" stroke="currentColor" stroke-width="1.6" stroke-linecap="round"/>
        <path d="M6 9.5l3.2 3.2L18 4" fill="none" stroke="currentColor" stroke-width="1.6" stroke-linecap="round" stroke-linejoin="round"/>
      </symbol>
      <linearGradient id="heartFill" x1="1" y1="0" x2="0.3" y2="1">
        <stop offset="0" stop-color="#f34a9a"/>
        <stop offset="1" stop-color="#cc1146"/>
      </linearGradient>
    </defs>
  </svg>

  <header class="topbar abs">
    <div class="brand">Lantern Row</div>
    <h1 class="page-title">Why me?</h1>
  </header>

  <section class="panel panel-hero abs">
    <div class="hero-figure abs" role="img" aria-label="Illustration of a caped superhero in blue and red flying forward"></div>
    <h2 class="serif-heading hero-title abs text-layer">If I was a<br>superhero</h2>
    <div class="rule" style="left:31px;top:127px;width:122px"></div>
    <p class="hero-intro abs text-layer">My four<br>superpowers<br>would be:</p>
    <div class="rule" style="left:31px;top:232px;width:122px"></div>
    <div class="hero-item abs text-layer" style="top:284px"><svg class="tick"><use href="#tick"/></svg>Proactiveness</div>
    <div class="hero-item abs text-layer" style="top:322px"><svg class="tick"><use href="#tick"/></svg>Creativity</div>
    <div class="hero-item abs text-layer" style="top:360px"><svg class="tick"><use href="#tick"/></svg>Pride in my work</div>
    <div class="hero-item abs text-layer" style="top:399px"><svg class="tick"><use href="#tick"/></svg>Organisational skills</div>
  </section>

  <section class="panel panel-success abs">
    <div class="trophy-figure abs" role="img" aria-label="Illustration of a celebrating businessman holding up a gold trophy"></div>
    <div class="rule" style="left:42px;top:47px;width:122px"></div>
    <h2 class="serif-heading success-title abs text-layer">Some of my<br>success</h2>
    <div class="rule" style="left:42px;top:140px;width:122px"></div>
    <div class="success-item abs text-layer" style="top:181px"><svg class="tick"><use href="#tick"/></svg><span>Increased client workshops<br>by 85% across accounts.</span></div>
    <div class="success-item abs text-layer" style="top:257px"><svg class="tick"><use href="#tick"/></svg><span>Delivered double digit<br>revenue increase.</span></div>
    <div class="success-item abs text-layer" style="top:326px"><svg class="tick"><use href="#tick"/></svg><span>Re-designed workshops<br>for virtual delivery,<br>maintaining key<br>relationships.</span></div>
  </section>

  <section class="panel panel-passion abs">
    <div class="rule" style="left:152px;top:30px;width:92px"></div>
    <h2 class="serif-heading passion-title abs">Passion</h2>
    <div class="rule" style="left:152px;top:68px;width:92px"></div>
    <svg class="heart abs" width="397" height="384" viewBox="0 0 397 384" aria-hidden="true">
      <path d="M198 68 L137 12 C100 -12 40 -6 0 38 L0 186 L198 383 L397 184 L397 50 C360 -6 300 -12 259 12 Z" fill="url(#heartFill)"/>
    </svg>
    <div class="passion-item abs" style="top:157px"><svg class="tick"><use href="#tick"/></svg>The development of others<br>and / or their teams.</div>
    <div class="passion-item abs" style="top:240px"><svg class="tick"><use href="#tick"/></svg>Helping people learn and be successful<br>in life and in their careers.</div>
    <div class="passion-item abs" style="top:325px"><svg class="tick"><use href="#tick"/></svg>Exceptional client<br>experiences</div>
  </section>

  <div class="divider divider-a abs"></div>
  <div class="divider divider-b abs"></div>

  <h2 class="serif-heading section-title abs">Why Lantern Row?</h2>

  <section class="feature feature-values abs">
    <svg class="feature-icon" viewBox="0 0 84 84" aria-hidden="true">
      <circle cx="42" cy="42" r="42" fill="var(--brand-blue)"/>
      <path d="M30 30h24l8 10-20 24-20-24z M22 40h40 M36 30l-4 10 10 24 10-24-4-10" fill="none" stroke="#fff" stroke-width="3" stroke-linejoin="round"/>
    </svg>
    <h3 class="serif-heading feature-heading">Values that stood out</h3>
    <div class="feature-rule"></div>
    <ul class="feature-list">
      <li><svg class="tick"><use href="#tick"/></svg>Change for the better</li>
      <li><svg class="tick"><use href="#tick"/></svg>Excellence – not mediocre</li>
      <li><svg class="tick"><use href="#tick"/></svg>Put your heart into it and give a shit</li>
      <li><svg class="tick"><use href="#tick"/></svg>Going the extra mile</li>
      <li><svg class="tick"><use href="#tick"/></svg>Take risks</li>
    </ul>
  </section>

  <section class="feature feature-offer abs">
    <svg class="feature-icon" viewBox="0 0 84 84" aria-hidden="true">
      <circle cx="42" cy="42" r="42" fill="var(--brand-blue)"/>
      <rect x="30" y="25" width="32" height="28" fill="none" stroke="#fff" stroke-width="3"/>
      <circle cx="29" cy="40" r="4" fill="#fff"/>
      <path d="M23 60v-10c0-3 3-5 6-5h4l10-8" fill="none" stroke="#fff" stroke-width="4" stroke-linecap="round"/>
      <path d="M38 45h14M22 62h44" stroke="#fff" stroke-width="3"/>
    </svg>
    <h3 class="serif-heading feature-heading">What you offer</h3>
    <div class="feature-rule"></div>
    <ul class="feature-list">
      <li><svg class="tick"><use href="#tick"/></svg>Learning &amp; Developing</li>
      <li><svg class="tick"><use href="#tick"/></svg>Team</li>
      <li><svg class="tick"><use href="#tick"/></svg>Flexibility</li>
      <li><svg class="tick"><use href="#tick"/></svg>Fun</li>
    </ul>
  </section>

  <section class="feature feature-projects abs">
    <svg class="feature-icon" viewBox="0 0 84 84" aria-hidden="true">
      <circle cx="42" cy="42" r="42" fill="var(--brand-blue)"/>
      <path d="M35 30v-5h14v5" fill="none" stroke="#fff" stroke-width="3"/>
      <rect x="22" y="30" width="40" height="28" rx="3" fill="none" stroke="#fff" stroke-width="3"/>
      <path d="M22 42h40" stroke="#fff" stroke-width="3"/>
      <rect x="38" y="39" width="8" height="6" fill="#fff"/>
    </svg>
    <h3 class="serif-heading feature-heading">Interesting projects</h3>
    <div class="feature-rule"></div>
    <div class="project"><strong>Veltra</strong>Leadership development and team effectiveness</div>
    <div class="project"><strong>Harlow &amp; Pike</strong>Change management for true transformation</div>
    <div class="project"><strong>Brandt's</strong>Customer centricity at Australia's most iconic<br>department store</div>
  </section>

  <footer class="footer abs">
    <p class="copyright">Copyright © 2022 All Rights Reserved</p>
  </footer>
</body>
</html>
```